Pet removal of legal foothold or snare traps trifold

A trifold that plainly describes how to remove your pet from a foot hold trap, Cable restraint or snare. Integrated with the Keystone Fieldcraft Guild logo,website and basic information about trapping.

Target Market(s)

Pet Owners ,General public ,outdoor enthusiasts ,hikers ,campers etc.

Industry/Entity Type

Legal

Requirements
Must have
• Keystone Fieldcraft Guild logo and website www.fieldcraftguild-example.org
• Pictures showing how to open a snare or cable restraint
• Pictures showing how to open a coil spring or long spring foothold trap
Nice to have
• I have some designs but I can't get them to download here I can email them to you
Should not have
• Anything that could be construed as anti-trapping

```html
<!DOCTYPE html>
<html lang="en">
<head>
<meta charset="utf-8">
<title>Keystone Fieldcraft Guild – Freeing Your Pet Trifold</title>
<link href="https://fonts.googleapis.com/css2?family=Montserrat:wght@700;800&family=Roboto:wght@400;500&family=Open+Sans:wght@400;600&display=swap" rel="stylesheet">
<style>
  :root{
    --crimson:#9c1b2e;
    --gold:#f4b41a;
    --sky:#2b8fd6;
    --ink:#1d1d1d;
    --paper:#ffffff;
    --stage:#e4e4e4;
  }
  *{margin:0;padding:0;box-sizing:border-box}
  html,body{width:1200px;height:898px;overflow:hidden}
  body{background:linear-gradient(135deg,#f1f1f1,var(--stage));position:relative;font-family:"Open Sans",sans-serif}
  .trifold{position:absolute;left:45px;top:29px;width:1110px;height:840px;display:flex;box-shadow:0 10px 30px rgba(0,0,0,.18)}
  .panel{position:relative;width:370px;height:840px;overflow:hidden;background:var(--paper)}
  .panel svg.art{position:absolute;inset:0;width:370px;height:840px}

  /* inside flap: release steps */
  .steps-title{position:absolute;top:368px;left:0;width:100%;text-align:center;font-family:"Montserrat",sans-serif;font-weight:800;font-size:30px;color:var(--gold)}
  .steps-body{position:absolute;top:418px;left:30px;right:30px;color:#fff;font-size:13px;line-height:1.5;text-align:justify}
  .steps-body strong{font-weight:600;color:var(--gold)}

  /* brand stand-in */
  .brand{position:absolute;left:0;width:100%;display:flex;flex-direction:column;align-items:center;gap:10px}
  .brand-dot{width:86px;height:86px;border-radius:50%;background:var(--crimson)}
  .brand-name{font-family:"Montserrat",sans-serif;font-weight:700;font-size:15px;color:var(--crimson);text-align:center;line-height:1.25}

  /* back panel */
  .phone{position:absolute;top:250px;width:100%;text-align:center;font-family:"Roboto",sans-serif;font-weight:500;font-size:38px;color:var(--sky);letter-spacing:1px}
  .web{position:absolute;top:302px;width:100%;text-align:center;font-family:"Roboto",sans-serif;font-size:16px;color:var(--ink)}

  /* cover */
  .headline{position:absolute;top:205px;width:100%;text-align:center}
  .headline .lead{display:block;font-family:"Montserrat",sans-serif;font-weight:800;font-size:32px;color:var(--crimson);letter-spacing:.5px}
  .headline .sub{display:block;font-family:"Montserrat",sans-serif;font-weight:700;font-size:24px;color:var(--ink);margin-top:2px}
  .web-pill{position:absolute;right:0;bottom:70px;background:var(--crimson);color:#fff;font-family:"Roboto",sans-serif;font-size:17px;letter-spacing:1.5px;padding:10px 22px 10px 26px;border-radius:24px 0 0 24px}
</style>
</head>
<body>
<main class="trifold">

  <!-- Inside flap: how to free a pet -->
  <section class="panel panel-steps">
    <svg class="art" viewBox="0 0 370 840">
      <defs>
        <linearGradient id="snareTone" x1="0" y1="0" x2="1" y2="1">
          <stop offset="0" stop-color="#7d7463"/><stop offset="1" stop-color="#4a3c2c"/>
        </linearGradient>
        <linearGradient id="footholdTone" x1="0" y1="0" x2="0" y2="1">
          <stop offset="0" stop-color="#9c1b2e"/><stop offset="1" stop-color="#5b4a44"/>
        </linearGradient>
      </defs>
      <rect role="img" aria-label="Photo: hands bending back the lock of a cable restraint to loosen the loop" x="0" y="0" width="370" height="340" fill="url(#snareTone)"/>
      <path d="M0,296 C120,326 250,296 370,221" fill="none" stroke="var(--crimson)" stroke-width="6"/>
      <path d="M0,306 C120,336 250,306 370,231" fill="none" stroke="var(--gold)" stroke-width="9"/>
      <path d="M0,317 C120,347 250,317 370,242" fill="none" stroke="var(--sky)" stroke-width="6"/>
      <path d="M0,327 C120,357 250,327 370,252 L370,840 L0,840Z" fill="var(--crimson)"/>
      <rect role="img" aria-label="Photo: feet pressing down both springs of a coil spring foothold trap to open the jaws" x="0" y="690" width="370" height="150" fill="url(#footholdTone)" opacity=".9"/>
    </svg>
    <h2 class="steps-title">Free Your Pet</h2>
    <p class="steps-body">Stay calm and keep your pet still; a held animal is rarely badly hurt. Cover its head with a coat to prevent bites. <strong>Snare or cable restraint:</strong> find the lock, bend it back against the cable and slide it open to loosen the loop, then lift it off. <strong>Coil spring foothold:</strong> stand on both spring levers until the jaws fall open, then ease the paw out. <strong>Long spring foothold:</strong> press the single spring flat under your foot. Then call the local game warden.</p>
  </section>

  <!-- Back panel: contact -->
  <section class="panel panel-contact">
    <svg class="art" viewBox="0 0 370 840">
      <defs>
        <linearGradient id="catchTone" x1="0" y1="0" x2="1" y2="1">
          <stop offset="0" stop-color="#8a8f86"/><stop offset="1" stop-color="#4d4a3e"/>
        </linearGradient>
      </defs>
      <path d="M196,690 C200,740 240,790 300,840" fill="none" stroke="var(--sky)" stroke-width="8"/>
      <path d="M214,690 C220,740 265,790 330,840" fill="none" stroke="var(--gold)" stroke-width="12"/>
      <path d="M232,685 C240,735 290,785 362,840" fill="none" stroke="var(--crimson)" stroke-width="9"/>
      <circle cx="180" cy="570" r="108" fill="var(--sky)"/>
      <circle cx="180" cy="570" r="101" fill="var(--paper)"/>
      <circle cx="180" cy="570" r="96" fill="var(--crimson)"/>
      <circle cx="180" cy="570" r="88" fill="var(--paper)"/>
      <circle role="img" aria-label="Photo: hands pressing open a long spring foothold trap" cx="180" cy="570" r="84" fill="url(#catchTone)"/>
    </svg>
    <div class="brand" style="top:90px">
      <span class="brand-dot"></span>
      <span class="brand-name">Keystone Fieldcraft Guild</span>
    </div>
    <p class="phone">555 014 2270</p>
    <p class="web">fieldcraftguild-example.org</p>
  </section>

  <!-- Front cover -->
  <section class="panel panel-cover">
    <svg class="art" viewBox="0 0 370 840">
      <defs>
        <linearGradient id="snowTone" x1="0" y1="0" x2="0" y2="1">
          <stop offset="0" stop-color="#a79d96"/><stop offset=".7" stop-color="#cfc8c2"/><stop offset="1" stop-color="#f2f2f2"/>
        </linearGradient>
      </defs>
      <path d="M120,330 C220,300 300,260 370,190" fill="none" stroke="var(--sky)" stroke-width="6"/>
      <path d="M150,345 C240,315 310,275 370,215" fill="none" stroke="var(--crimson)" stroke-width="9"/>
      <path d="M0,415 C110,365 250,345 370,255" fill="none" stroke="var(--crimson)" stroke-width="8"/>
      <path d="M0,430 C110,380 250,360 370,270" fill="none" stroke="var(--gold)" stroke-width="10"/>
      <path d="M0,445 C110,395 250,375 370,285" fill="none" stroke="var(--sky)" stroke-width="7"/>
      <path role="img" aria-label="Photo: dog walking safely on a snowy trail" d="M0,458 C110,408 250,388 370,298 L370,840 L0,840Z" fill="url(#snowTone)"/>
    </svg>
    <div class="brand" style="top:40px">
      <span class="brand-dot"></span>
      <span class="brand-name">Keystone Fieldcraft Guild</span>
    </div>
    <h1 class="headline"><span class="lead">FREEING A PET</span><span class="sub">from a legal trap</span></h1>
    <p class="web-pill">fieldcraftguild-example.org</p>
  </section>

</main>
</body>
</html>
```